International Petrochemical business needs a web design for Tessaro Desk system

We need a web design for a "Tessaro Desk" system for an international petrochemical company. The web site is used internally within the company. It is hosted by an internal department which provides government permit request service for other departments.

We would like to see designs of two pages using color light blue. (home page, internal page as attached).
Home Page:
1. Header has a background image and small animation. Header on home page can be taller than the header of the internal page.
2. Layout as attached.

Internal Page:
1. Header can use the same background image as the home page and can be shorter to utilize the page for content.
2. The blue icon behind every captions represent an icon. When user move mouse over this icon, it displays the caption in Thai language as a tooltip. This icon needs to be redesign.

The final design should communicate the followings:
- Excellent service provided system in terms of time and accurary
- Rapid growth of business via building petrochemical refinery plant

For Internal Page, the blue circle behind every captions represent an icon. When mouse over this icon, a tool tip showing the caption in Thai language is shown. Please also design this icon..

There are more feedbacks from customer as followed:

1. Banner should consists of 
    1.1 "Approved" stamp on paper
    1.2 An image of Garuda. It is used on every government documents in Thailand
    1.3 Image of petrochemical plant
2. Each menu item (Home, Permit, Search, etc) should have different colors. Drop down menu will use the same color as its parent menu item.
3. Overall tone of the web page should be light blue with background of the body the web page in white
4. "New Request" button should use green color with icon on it
5. Table header of each box in the body of the page should use dark blue background with text in white

Please kindly submit your revisions.
Thank you.

Reason: We get some late feedbacks from customers which was just updated to all designers.

• 1. Design for 1024x768 screen resolution
2. Use light blue theme
3. Background of header where the company logo is must have white background

```html
<!DOCTYPE html>
<html lang="en">
<head>
<meta charset="utf-8">
<title>Tessaro Desk – Request Form</title>
<link rel="stylesheet" href="https://fonts.googleapis.com/css2?family=Cabin:wght@400;500;600;700&family=Arimo:wght@400;700&display=swap">
<style>
:root{
  --sky:#cdeefb;
  --sky-soft:#e6f7fd;
  --navy:#1b2a6b;
  --brand:#1aa0e0;
  --label:#2a7fbf;
  --accent-red:#e3262b;
  --line:#9fd3ec;
  --field-border:#555;
  --btn-dark:#2f5a9e;
  --btn-cyan:#1aaae2;
  --footer:#0a8ac8;
  --text:#333;
  --white:#fff;
}
*{box-sizing:border-box;margin:0;padding:0}
html,body{width:945px;height:1200px;overflow:hidden}
body{position:relative;font-family:"Cabin",Arial,sans-serif;color:var(--text);
  background:linear-gradient(180deg,var(--sky) 0,var(--sky) 600px,#f4fbfe 740px,#fff 800px)}
.abs{position:absolute}
.brand{left:20px;top:22px;display:flex;align-items:center;gap:6px;font-family:"Cabin",sans-serif;font-weight:700;font-size:16px;color:var(--brand);text-transform:uppercase;line-height:1}
.brand-dot{width:30px;height:30px;border-radius:50%;background:var(--brand)}
.system-name{right:22px;top:12px;font-family:"Cabin",sans-serif;font-weight:500;font-size:19px;letter-spacing:.6px;color:var(--navy)}
.nav{left:217px;top:52px;width:711px;height:38px;background:var(--white);border-radius:6px 6px 0 0}
.nav a{position:absolute;top:0;height:38px;line-height:40px;font-family:"Cabin",sans-serif;font-size:13px;font-weight:500;color:var(--brand);text-decoration:none;text-align:center}
.nav a.active{color:var(--accent-red);border-top:2px solid var(--accent-red);line-height:36px}
.nav .sep{position:absolute;top:6px;width:1px;height:30px;background:#e4eef4}
.search{left:740px;top:60px;width:174px;height:22px;border:1px solid var(--navy);background:#fff;font-family:"Cabin",sans-serif;font-style:italic;font-size:10px;color:#777;padding:4px 0 0 32px}
.search svg{position:absolute;right:2px;top:2px}
.banner{left:16px;top:90px;width:913px;height:85px;background:linear-gradient(90deg,#27377f 0%,#3b5aa8 45%,#4a6cb6 70%,#2f4690 100%)}
.page-title{left:42px;top:125px;font-family:"Cabin",sans-serif;font-size:21px;font-weight:500;color:#fff}
.content{left:16px;top:175px;width:913px;height:905px;background:#fff}
.form-panel{left:33px;top:193px;width:679px;height:876px;border:1px solid var(--line);border-radius:6px;background:linear-gradient(180deg,#eef9fe 0,#fff 40px)}
.form-title{left:53px;top:199px;font-family:"Cabin",sans-serif;font-size:15px;font-weight:500;color:var(--accent-red)}
.lbl{font-family:"Cabin",sans-serif;font-weight:600;font-size:11.5px;color:var(--label);white-space:nowrap}
.val{font-size:11px;color:#333}
.info-icon{display:inline-block;width:11px;height:11px;border-radius:50%;background:#3a5ea8;border:2px solid #e9566a;vertical-align:-1px;margin:0 1px}
.field{border:1px solid var(--field-border);border-radius:4px;background:#fff;font-size:10px;color:#444;padding-left:23px;display:flex;align-items:center}
.field.select::after{content:"";position:absolute;right:8px;top:8px;border:6px solid transparent;border-top:8px solid #999}
.area{border:1px solid var(--field-border);border-radius:4px;background:#fff;font-size:10px;color:#444;padding:12px 0 0 23px;line-height:18px}
.btn{background:linear-gradient(180deg,#4d76bd,var(--btn-dark));color:#fff;border-radius:4px;font-family:"Cabin",sans-serif;font-size:11px;font-weight:500;text-align:center;letter-spacing:.4px}
.del{display:inline-block;width:11px;height:11px;border-radius:50%;background:var(--accent-red);vertical-align:-1px;margin-left:6px}
.item{font-size:10.5px;color:#444}
.new-req{left:496px;top:402px;font-family:"Cabin",sans-serif;font-size:15px;font-weight:600;color:var(--brand)}
.related{left:183px;top:896px;width:418px;height:95px;border:1px solid #555;border-radius:4px;overflow:hidden;font-size:10.5px}
.related table{width:100%;border-collapse:collapse}
.related th{height:25px;font-weight:400;color:#333;background:linear-gradient(180deg,#fff,#e6e6e6);border-bottom:1px solid #555;border-left:1px solid #555;text-align:left;padding-left:17px}
.related th:first-child{border-left:0}
.related td{height:18px;padding-left:17px;border-left:1px solid #555;color:#444}
.related td:first-child{border-left:0;color:var(--brand)}
.related tr:first-child td{padding-top:6px;height:22px}
.related .fill td{height:22px}
.pager{left:513px;top:1000px;width:84px;height:18px;border-radius:4px;background:var(--btn-dark);color:#fff;font-size:10px;font-weight:700;display:flex;justify-content:space-around;align-items:center;padding:0 4px}
.pager .cur{color:var(--accent-red)}
.create{left:181px;top:1034px;width:231px;height:28px;border-radius:6px;background:var(--btn-cyan);color:#fff;font-family:"Cabin",sans-serif;font-size:16px;font-weight:500;padding:4px 0 0 21px}
.create span{font-size:11px;margin-left:14px}
.side{left:722px;top:192px;width:195px;height:306px;border:1px solid var(--line);border-radius:6px;background:#fff}
.side-inner{left:730px;top:201px;width:179px;height:287px;background:#c8eaf8;border-radius:4px}
.side-title{left:737px;top:212px;font-family:"Cabin",sans-serif;font-weight:600;font-size:21px;line-height:26px;color:var(--label)}
.help-visual{left:841px;top:211px;width:62px;height:62px;border-radius:4px;background:linear-gradient(135deg,#f2b8b8,#e8e8e8)}
.faq{left:745px;top:284px;list-style:none;font-family:"Cabin",sans-serif;font-size:11.5px;font-weight:500;color:#444}
.faq li{height:19.4px}
.faq li::before{content:">";color:var(--label);margin-right:6px;font-weight:700}
.help{left:819px;top:446px;width:79px;height:23px;border-radius:5px;background:linear-gradient(180deg,#ff5b5b,#e01c1c);color:#fff;font-family:"Cabin",sans-serif;font-size:11px;font-weight:600;text-align:center;line-height:23px}
.footer{left:0;top:1080px;width:945px;height:120px;background:var(--footer)}
.footer-image{left:185px;top:1106px;width:558px;height:58px;background:linear-gradient(90deg,#1c3f9a 0%,#2e6ad0 45%,#a9d9f2 62%,#d8eff9 100%)}
.footer-image span{position:absolute;left:334px;top:20px;font-family:"Cabin",sans-serif;font-size:12px;color:#333}
.footer-text{left:0;width:945px;top:1173px;text-align:center;font-family:"Cabin",sans-serif;font-size:12px;color:#fff}
</style>
</head>
<body>
<header>
  <div class="abs brand"><span class="brand-dot"></span>Norvane Chemical</div>
  <div class="abs system-name">TESSARO DESK</div>
  <nav class="abs nav">
    <a style="left:10px;width:86px" href="#">HOME</a><i class="sep" style="left:96px"></i>
    <a class="active" style="left:96px;width:88px" href="#">PERMITS</a><i class="sep" style="left:184px"></i>
    <a style="left:184px;width:92px" href="#">SEARCH</a><i class="sep" style="left:276px"></i>
    <a style="left:276px;width:88px" href="#">REPORT</a><i class="sep" style="left:364px"></i>
    <a style="left:364px;width:78px" href="#">ADMIN</a><i class="sep" style="left:442px"></i>
    <a style="left:442px;width:68px" href="#">HELP</a>
  </nav>
  <div class="abs search">Keyword Search
    <svg width="18" height="18" viewBox="0 0 18 18"><circle cx="7" cy="7" r="5" fill="none" stroke="#1aa0e0" stroke-width="2.5"/><line x1="11" y1="11" x2="16" y2="16" stroke="#1aa0e0" stroke-width="3" stroke-linecap="round"/></svg>
  </div>
  <div class="abs banner" role="img" aria-label="Petrochemical plant towers and pipes under a blue sky"></div>
  <h1 class="abs page-title">Page Title Goes Here</h1>
</header>

<main>
  <div class="abs content"></div>
  <section class="abs form-panel"></section>
  <h2 class="abs form-title">Request Form</h2>

  <div class="abs lbl" style="left:52px;top:234px">Request Date :</div>
  <div class="abs val" style="left:167px;top:234px">dd/mm/yyyy</div>
  <div class="abs lbl" style="left:350px;top:234px;font-size:10.5px">Employee No :</div>
  <div class="abs val" style="left:433px;top:235px;font-size:10px">xxxxxxxx</div>
  <div class="abs lbl" style="left:52px;top:264px">Requester Name :</div>
  <div class="abs val" style="left:167px;top:264px">Alan Reed</div>
  <div class="abs lbl" style="left:350px;top:263px;font-size:10.5px">Telephone :</div>
  <div class="abs val" style="left:433px;top:264px;font-size:10px">xxxx</div>

  <div class="abs lbl" style="left:52px;top:293px">Contact No <i class="info-icon"></i> :</div>
  <div class="abs field" style="left:182px;top:290px;width:186px;height:25px">xxxxxxxx</div>
  <div class="abs lbl" style="left:52px;top:323px">Company <i class="info-icon"></i> :</div>
  <div class="abs field select" style="left:182px;top:321px;width:186px;height:25px">Please Select ...</div>
  <div class="abs lbl" style="left:52px;top:353px">Branch<i class="info-icon"></i>:</div>
  <div class="abs field select" style="left:182px;top:353px;width:186px;height:25px">Please Select ...</div>
  <div class="abs lbl" style="left:52px;top:383px">Document Category &nbsp;&nbsp;:</div>
  <div class="abs field select" style="left:182px;top:381px;width:186px;height:25px">Please Select ...</div>
  <div class="abs lbl" style="left:52px;top:413px">Document Type<i class="info-icon"></i>:</div>
  <div class="abs field select" style="left:182px;top:412px;width:186px;height:25px">Please Select ...</div>
  <div class="abs new-req">New Requests</div>
  <div class="abs lbl" style="left:52px;top:443px">Expected Use Date<i class="info-icon"></i>:</div>
  <div class="abs field" style="left:182px;top:444px;width:123px;height:24px">DD/MM/YYYY</div>
  <div class="abs lbl" style="left:52px;top:473px">Detail<i class="info-icon"></i>:</div>
  <div class="abs area" style="left:182px;top:475px;width:418px;height:95px">xxxxxxxx<br>xxxxxxxxxxxxxxxxx</div>

  <div class="abs lbl" style="left:52px;top:581px">Attachment<i class="info-icon"></i>:</div>
  <div class="abs field" style="left:182px;top:577px;width:233px;height:25px"></div>
  <div class="abs btn" style="left:425px;top:579px;width:83px;height:19px;line-height:19px">BROWSE</div>
  <div class="abs btn" style="left:517px;top:579px;width:83px;height:19px;line-height:19px">ATTACH</div>
  <div class="abs item" style="left:187px;top:606px">File1.docx<i class="del"></i></div>
  <div class="abs item" style="left:187px;top:624px">File2.docx<i class="del"></i></div>

  <div class="abs lbl" style="left:52px;top:656px">Coordinator<i class="info-icon"></i>:</div>
  <div class="abs btn" style="left:175px;top:653px;width:83px;height:18px;line-height:18px">ADD</div>
  <div class="abs item" style="left:187px;top:683px">Alan Reed (HR)<i class="del"></i></div>

  <div class="abs lbl" style="left:52px;top:716px">Related Person<i class="info-icon"></i>:</div>
  <div class="abs btn" style="left:175px;top:714px;width:83px;height:18px;line-height:18px">ADD</div>
  <div class="abs item" style="left:187px;top:744px">Nora Vale (IT)<i class="del" style="margin-left:12px"></i></div>
  <div class="abs item" style="left:187px;top:767px">Tim Cole (Accounting)<i class="del" style="margin-left:14px"></i></div>

  <div class="abs lbl" style="left:52px;top:791px">Remark<i class="info-icon"></i>:</div>
  <div class="abs area" style="left:182px;top:789px;width:418px;height:95px">xxxxxxxx<br>xxxxxxxxxxxxxxxxx</div>

  <div class="abs lbl" style="left:52px;top:896px">Related Request<i class="info-icon"></i>:</div>
  <div class="abs related">
    <table>
      <thead><tr><th style="width:110px">Request No.</th><th style="width:119px">Request Date</th><th style="width:93px">Company</th><th>Branch</th></tr></thead>
      <tbody>
        <tr><td>yy-xxxx</td><td>DD/MM/YYYY</td><td>ABC</td><td>GC1</td></tr>
        <tr><td>yy-xxxx</td><td>DD/MM/YYYY</td><td>XYZ</td><td>GC2</td></tr>
        <tr><td>yy-xxxx</td><td>DD/MM/YYYY</td><td>XYZ</td><td>GC3</td></tr>
        <tr class="fill"><td></td><td></td><td></td><td></td></tr>
      </tbody>
    </table>
  </div>
  <div class="abs pager"><span>&lt;</span><span class="cur">1</span><span>2</span><span>3</span><span>4</span><span>&gt;</span></div>

  <div class="abs create">Create New Requests<span>&#9654;</span></div>
  <div class="abs btn" style="left:512px;top:1038px;width:83px;height:18px;line-height:18px">BACK</div>

  <aside>
    <div class="abs side"></div>
    <div class="abs side-inner"></div>
    <h3 class="abs side-title">Common<br>Questions</h3>
    <div class="abs help-visual" role="img" aria-label="Lifebuoy illustration for help"></div>
    <ul class="abs faq">
      <li>Lorem ipsum dolor sit</li>
      <li>Pamet, consectetur</li>
      <li>Ladipisicing elit, sed do</li>
      <li>Heiusmod tempor</li>
      <li>Kincididunt ut labore et</li>
      <li>Adolore magna aliqua.</li>
      <li>Ut enim ad minim</li>
      <li>Veniam, quis nostrud e</li>
    </ul>
    <div class="abs help">GET HELP</div>
  </aside>
</main>

<footer>
  <div class="abs footer"></div>
  <div class="abs footer-image" role="img" aria-label="Blue molecular structure graphic"><span>IMAGE GOES HERE</span></div>
  <div class="abs footer-text">Footer texts go here</div>
</footer>
</body>
</html>
```